luxury residential property maintenance & construction company needs fleet vehicle wrap design

need fleet vehicle wrap design for multiple pickup truck and transit vans for residential property maintenance and construction company. Cater to luxury multi-million dollar homes located in very affluent neighborhoods and private communities. Looking for a visible but classy and clean design that looks elegant.

```html
<!DOCTYPE html>
<html lang="en">
<head>
<meta charset="utf-8">
<title>Ardenmoor Living – Fleet Wrap</title>
<link rel="stylesheet" href="https://fonts.googleapis.com/css2?family=Cormorant+Garamond:wght@500&family=Tinos:wght@700&family=Open+Sans:wght@400&display=swap">
<style>
  :root {
    --wrap-white: #ffffff;
    --brand-green: #4c7a5d;
    --brand-green-deep: #2f5a40;
    --ink: #141414;
    --steel-light: #d9dcdd;
    --steel-dark: #6e7274;
    --canvas: #eceeed;
  }
  html, body {
    margin: 0;
    padding: 0;
    width: 1200px;
    height: 996px;
    overflow: hidden;
    background: var(--canvas);
  }
  .fleet-sheet {
    width: 1200px;
    height: 996px;
    display: flex;
    flex-direction: column;
  }
  .wrap-panel { display: block; width: 1200px; }
  .wrap-panel--truck { height: 462px; }
  .wrap-panel--van { height: 534px; }
  .brand-name {
    font-family: "Cormorant Garamond", serif;
    font-weight: 500;
    fill: var(--ink);
  }
  .brand-sub {
    font-family: "Open Sans", sans-serif;
    font-weight: 400;
    fill: var(--ink);
  }
  .brand-rule { stroke: var(--brand-green); stroke-width: 1.5; }
  .contact-phone {
    font-family: "Tinos", serif;
    font-weight: 700;
    fill: var(--wrap-white);
  }
  .contact-web {
    font-family: "Open Sans", sans-serif;
    font-weight: 400;
    fill: var(--wrap-white);
  }
</style>
</head>
<body>
<main class="fleet-sheet">

  <!-- Pickup truck side -->
  <svg class="wrap-panel wrap-panel--truck" viewBox="0 0 1200 462" xmlns="http://www.w3.org/2000/svg">
    <defs>
      <linearGradient id="truckSteel" x1="0" y1="0" x2="1" y2="1">
        <stop offset="0" stop-color="var(--steel-light)"/>
        <stop offset="1" stop-color="var(--steel-dark)"/>
      </linearGradient>
      <linearGradient id="truckGreen" x1="0" y1="0" x2="1" y2="1">
        <stop offset="0" stop-color="var(--brand-green-deep)"/>
        <stop offset="1" stop-color="var(--brand-green)"/>
      </linearGradient>
    </defs>
    <rect class="wrap-base" x="30" y="40" width="1140" height="320" rx="18" fill="var(--wrap-white)"/>
    <path class="building-photo" role="img" aria-label="Modern architecture facade photograph"
          d="M690 40 L1170 40 L1170 340 Q1170 360 1150 360 L530 360 L580 305 L780 215 Z"
          fill="url(#truckSteel)"/>
    <path class="accent-arc" d="M775 360 C785 250 845 170 965 130" fill="none" stroke="var(--brand-green)" stroke-width="4"/>
    <path class="green-field" role="img" aria-label="Green tinted building facade photograph"
          d="M800 360 C810 250 875 170 995 130 L1170 130 L1170 340 Q1170 360 1150 360 Z"
          fill="url(#truckGreen)" opacity="0.95"/>

    <circle class="brand-dot" cx="352" cy="239" r="48" fill="none" stroke="var(--brand-green)" stroke-width="6"/>
    <text class="brand-name" x="425" y="233" font-size="38" textLength="271" lengthAdjust="spacing">ARDENMOOR</text>
    <line class="brand-rule" x1="425" y1="248" x2="497" y2="248"/>
    <text class="brand-sub" x="560" y="253" font-size="13" text-anchor="middle" letter-spacing="5">LIVING</text>
    <line class="brand-rule" x1="624" y1="248" x2="696" y2="248"/>

    <circle class="phone-badge" cx="928" cy="167" r="11" fill="var(--wrap-white)"/>
    <path class="phone-icon" d="M923 162 q1 -2 3 -1 l2 3 q0 1 -1 2 q1 3 4 4 q1 -1 2 -1 l3 2 q1 2 -1 3 q-6 1 -11 -5 q-3 -4 -1 -7z" fill="var(--brand-green-deep)"/>
    <text class="contact-phone" x="945" y="176" font-size="24" textLength="140" lengthAdjust="spacingAndGlyphs">+014 5550 182</text>
    <text class="contact-web" x="897" y="194" font-size="11" textLength="208" lengthAdjust="spacing">WWW.ARDENMOORLIVING.COM</text>
  </svg>

  <!-- Transit van side -->
  <svg class="wrap-panel wrap-panel--van" viewBox="0 0 1200 534" xmlns="http://www.w3.org/2000/svg">
    <defs>
      <linearGradient id="vanSteel" x1="0" y1="0" x2="1" y2="1">
        <stop offset="0" stop-color="var(--steel-light)"/>
        <stop offset="1" stop-color="var(--steel-dark)"/>
      </linearGradient>
      <linearGradient id="vanGreen" x1="0" y1="0" x2="1" y2="1">
        <stop offset="0" stop-color="var(--brand-green-deep)"/>
        <stop offset="1" stop-color="var(--brand-green)"/>
      </linearGradient>
    </defs>
    <rect class="wrap-base" x="30" y="20" width="1140" height="480" rx="22" fill="var(--wrap-white)"/>
    <path class="building-photo" role="img" aria-label="Modern architecture facade photograph"
          d="M650 20 L1150 20 Q1170 20 1170 40 L1170 480 Q1170 500 1150 500 L520 500 L560 482 L800 440 L795 330 Z"
          fill="url(#vanSteel)"/>
    <path class="accent-arc" d="M805 500 C765 360 795 140 910 30" fill="none" stroke="var(--brand-green)" stroke-width="5"/>
    <path class="green-field" role="img" aria-label="Green tinted building facade photograph"
          d="M832 500 C792 360 820 150 940 30 L1150 30 Q1170 30 1170 50 L1170 480 Q1170 500 1150 500 Z"
          fill="url(#vanGreen)" opacity="0.95"/>

    <circle class="brand-dot" cx="548" cy="215" r="92" fill="none" stroke="var(--brand-green)" stroke-width="12"/>
    <text class="brand-name" x="334" y="380" font-size="56" textLength="428" lengthAdjust="spacing">ARDENMOOR</text>
    <line class="brand-rule" x1="334" y1="409" x2="442" y2="409"/>
    <text class="brand-sub" x="548" y="417" font-size="22" text-anchor="middle" letter-spacing="9">LIVING</text>
    <line class="brand-rule" x1="652" y1="409" x2="762" y2="409"/>

    <circle class="phone-badge" cx="842" cy="236" r="14" fill="var(--wrap-white)"/>
    <path class="phone-icon" d="M836 230 q1 -2 3 -1 l3 4 q0 1 -1 2 q1 4 5 5 q1 -1 2 -1 l4 3 q1 2 -1 3 q-7 1 -13 -6 q-4 -5 -2 -9z" fill="var(--brand-green-deep)"/>
    <text class="contact-phone" x="862" y="248" font-size="32" textLength="184" lengthAdjust="spacingAndGlyphs">+014 5550 182</text>
    <text class="contact-web" x="800" y="272" font-size="13" textLength="270" lengthAdjust="spacing">WWW.ARDENMOORLIVING.COM</text>
  </svg>

</main>
</body>
</html>
```